GUARANTEED WordPress design needed for a sassy, confident charisma coach!

We need a website design for Marla Penrick's brand new, responsive, Wordpress website.
Marla is a trainer / coach who teaches people how to be more charismatic and runs events, publishes video courses and has an ongoing video blog. Her old website is here: www.marlapenrick.co.uk ... but it's now time to have a much better site!
We have a strong idea about the technical components of the website, but we need a designer's eye to create a great style for the site (and provide layered PSD files which our developers will then convert to HTML and CSS).
Marla's brand is sassy, brave, warm and confident. The videos on her existing site give quite a good feel for her personality. We need a clean, stylish and compelling page that isn't too corporate and captures her personality. Every element needs to feel coherent, from fonts and headings to colours and spacing.
The following sites are not exactly what Marla wants (and certainly aren't right in terms of colours) but they give you an idea of the kind of people she is competing against and the area she is operating in:
http://www.tessa-broughley.example/
http://rowanfelsby.example/
Ideally, you will have done something similar and be able to key in on exactly the kind of thing we want: we're not looking to reinvent the wheel. Hopefully you won't mind tweaking a few things if you are close to what we need.
More detail is provided in the word document attached. But in a nutshell we need: a banner, footer, sign-up strap, menu bar, signature and 4 different basic page types. We want bursts of bright colours, contrasted with black and white if possible - sorry we can't be more specific than that...
The word doc also contains some amateur mock-ups as well (the images are also just mockups at this stage) - but although these give a general sense of the structure what we are looking for, we are clearly not designers...so please help! We need a designer's touch!
Kind regards,
Corin
PS The layered PSD versions of the mockup files are available on Cloudvantre: https://files.cloudvantre.example/sh/k72pqa4w1zbtmrd/QXvenlr8Ty3PwMiU6Hs2kYfDb?dl=0
Target Market(s)
Entrepreneurs who need to sell themselves.
Number of Pages Required
4 page

```html
<!DOCTYPE html>
<html lang="en">
<head>
<meta charset="utf-8">
<title>Marla Penrick</title>
<link href="https://fonts.googleapis.com/css2?family=Raleway:wght@400;500;600&family=Open+Sans:ital,wght@0,400;0,600;1,400&display=swap" rel="stylesheet">
<style>
:root{
  --pink:#c90f7c;
  --green:#7dba1f;
  --ink:#222;
  --muted:#555;
  --page:#efefef;
  --card:#fff;
  --line:#e2e2e2;
  --fb:#3b5998;
  --tw:#1da1f2;
  --li:#1b4f8a;
  --hero-tone-a:#f1eded;
  --hero-tone-b:#e7c4c5;
}
*{box-sizing:border-box;margin:0;padding:0}
html,body{width:726px;height:1200px;overflow:hidden}
body{position:relative;background:var(--page);font-family:"Open Sans",Arial,sans-serif;color:var(--ink)}
.abs{position:absolute}
.header{left:0;top:0;width:726px;height:43px;background:#fafafa}
.brand{left:53px;top:9px;font-family:"Raleway",sans-serif;font-weight:500;font-size:21px;color:var(--pink)}
.nav{left:322px;top:0;display:flex;gap:12px;font-family:"Raleway",sans-serif;font-size:7.6px;font-weight:600}
.nav span{padding-top:19px;height:43px;color:#333}
.nav .active{color:var(--pink);border-top:2px solid var(--pink);padding-top:17px}
.social{display:flex;gap:5px}
.dot{width:16px;height:16px;border-radius:50%;display:block}
.dot.fb{background:var(--fb)}.dot.tw{background:var(--tw)}.dot.li{background:var(--li)}
.hero{left:0;top:43px;width:726px;height:280px;background:linear-gradient(100deg,#fff 45%,#f1f1f1 75%,#e4e4e4)}
.hero-photo{left:392px;top:64px;width:170px;height:259px;background:linear-gradient(180deg,var(--hero-tone-a),var(--hero-tone-b))}
.hero-kicker{left:53px;top:120px;font-family:"Raleway",sans-serif;font-size:17px}
.hero-title{left:52px;top:134px;font-family:"Raleway",sans-serif;font-size:37.5px;color:var(--pink);font-weight:500}
.hero-copy{left:53px;top:184px;width:310px;font-size:7px;line-height:13px;color:#333}
.btn{background:var(--pink);color:#fff;font-size:7px;font-weight:600;display:flex;align-items:center;justify-content:center}
.hero-btn{left:54px;top:216px;width:67px;height:25px}
.strap{left:0;top:323px;width:726px;height:74px;background:var(--pink)}
.strap-device{left:128px;top:300px;width:108px;height:90px;background:linear-gradient(160deg,#ddd,#888 60%,#c8c8c8);border-radius:4px;transform:rotate(-9deg)}
.strap-text{left:276px;top:330px;width:270px;color:#fff;font-size:6.6px;line-height:11.5px}
.field{background:#fff;border:1px solid #ddd;font-size:8px;color:#444;padding-left:8px;display:flex;align-items:center}
.strap-name{left:274px;top:357px;width:131px;height:20px}
.strap-email{left:409px;top:357px;width:131px;height:20px}
.yes{border-radius:50%;background:var(--green);color:#fff;font-size:7px;text-align:center;display:flex;align-items:center;justify-content:center;line-height:9px;border:2px solid #fff}
.strap-yes{left:545px;top:355px;width:34px;height:34px;border-color:var(--green)}
.strap-note{left:272px;top:381px;color:#fff;font-size:6.6px;font-weight:600}
.card{background:var(--card);border:1px solid var(--line)}
.h{font-family:"Raleway",sans-serif;font-size:13px}
.h em{font-style:normal;color:var(--pink)}
.video-card{left:54px;top:413px;width:430px;height:202px}
.video{left:63px;top:445px;width:412px;height:161px;background:radial-gradient(circle at 50% 40%,#4a4a4a,#1c1c1c 70%)}
.play{left:258px;top:510px}
.video-label{left:0;width:412px;top:90px;text-align:center;color:#ddd;font-size:6.4px}
.tweets{left:497px;top:413px;width:174px;height:176px}
.tweet{position:absolute;left:9px;width:148px;font-size:6px;color:#333;line-height:9px}
.avatar{position:absolute;left:0;top:0;width:17px;height:17px;background:#8a6a5e}
.tweet .body{padding-left:22px}
.tweet b{font-weight:600}
.tweet .handle{color:#999}
.tweet a{color:var(--tw);text-decoration:none}
.partners{left:497px;top:603px;width:174px;height:245px}
.badge{position:absolute;width:62px;height:22px;background:#dcdcdc;border-radius:3px}
.aud{top:630px;width:211px;height:223px}
.aud-photo{position:absolute;left:6px;top:6px;width:199px;height:152px}
.aud h3{position:absolute;left:6px;top:166px;font-family:"Raleway",sans-serif;font-weight:400;font-size:11.5px}
.aud p{position:absolute;left:6px;top:185px;width:200px;font-size:6.6px;line-height:12px;color:#333}
.stories{left:54px;top:868px;width:430px;height:144px}
.pol{position:absolute;width:60px;height:86px;background:#fff;box-shadow:0 1px 3px rgba(0,0,0,.35);padding:4px}
.pol div{width:100%;height:100%}
.quote{position:absolute;width:108px;font-size:6.3px;line-height:9.8px;color:#333;text-align:justify}
.quote i{display:block;color:var(--pink);font-size:7px;margin-top:4px}
.quote span{display:block;margin-top:3px}
.tips{left:497px;top:862px;width:174px;height:144px}
.tip-img{position:absolute;left:9px;width:74px;height:42px}
.tip{position:absolute;left:89px;width:70px;font-size:6.3px;line-height:10px;color:#444}
.tip span{color:var(--pink);display:block}
.news{left:0;top:1033px;width:726px;height:143px;background:#fff;text-align:center}
.news h2{position:absolute;top:10px;width:726px;font-family:"Open Sans",sans-serif;font-weight:400;font-size:13.5px;letter-spacing:.5px}
.news p{position:absolute;left:213px;top:32px;width:300px;font-size:6.6px;line-height:12px;color:#444}
.news-first{left:219px;top:1100px;width:143px;height:20px}
.news-email{left:369px;top:1100px;width:143px;height:20px}
.news-yes{left:519px;top:1092px;width:35px;height:35px;border-color:var(--green)}
.news-sad{left:0;top:1126px;width:726px;text-align:center;font-size:6.6px}
.news-social{left:329px;top:1142px}
.news-social .dot{width:19px;height:19px;margin-right:5px}
.footer{left:0;top:1176px;width:726px;height:24px;background:var(--pink);color:#fff;font-size:6.4px}
.footer .copy{position:absolute;left:53px;top:8px}
.footer .links{position:absolute;right:54px;top:8px;display:flex;gap:10px}
</style>
</head>
<body>
<header class="abs header"></header>
<div class="abs brand">Marla Penrick</div>
<nav class="abs nav">
  <span class="active">HOME</span><span>EVENTS</span><span>WORK WITH ME</span><span>CORPORATE</span><span>ABOUT</span><span>CONTACT</span>
  <span class="social" style="padding-top:13px"><i class="dot fb"></i><i class="dot tw"></i><i class="dot li"></i></span>
</nav>

<section class="abs hero"></section>
<div class="abs hero-photo" role="img" aria-label="Portrait photo of the coach"></div>
<div class="abs hero-kicker">Attract</div>
<h1 class="abs hero-title">Connect Influnece</h1>
<p class="abs hero-copy">Lorem Ipsum is simply dummy text of the printing and typesetting industry. Lorem Ipsum has been the industry's standard dummy text ever since the 1500s.</p>
<div class="abs btn hero-btn">Read More</div>

<section class="abs strap"></section>
<div class="abs strap-device" role="img" aria-label="Desktop monitor showing the free training video"></div>
<p class="abs strap-text">Learn how to unlock the superpower* of your charisma and win all the business you want with this free training."</p>
<div class="abs field strap-name">Name</div>
<div class="abs field strap-email">Email</div>
<div class="abs yes strap-yes">YES<br>PLEASE</div>
<div class="abs strap-note">* Promise to only use your powers for good</div>

<section class="abs card video-card"><h2 class="h" style="position:absolute;left:9px;top:10px;font-weight:400">WATCH <em>VIDEO</em></h2></section>
<div class="abs video" role="img" aria-label="Video still of the coach">
  <div class="abs video-label">VIDEO PLACEHOLDER</div>
</div>
<svg class="abs play" width="18" height="18" viewBox="0 0 18 18"><circle cx="9" cy="9" r="8" fill="none" stroke="#fff" stroke-width="1"/><path d="M7 5.5v7l5.5-3.5z" fill="#fff"/></svg>

<aside class="abs card tweets">
  <h2 class="h" style="position:absolute;left:9px;top:6px;font-weight:400;font-size:11.5px">Tweets <em style="font-size:6.5px;font-family:'Open Sans',sans-serif">by @marlapenrickltd</em></h2>
  <div style="position:absolute;right:6px;top:8px;width:3px;height:16px;background:var(--pink)"></div>
  <div class="tweet" style="top:28px"><div class="avatar" role="img" aria-label="Profile photo"></div><div class="body"><b>Marla Penrick</b><br><span class="handle">@marlapenrickltd</span></div><div style="margin-top:4px"><a>#mondaymotivation</a> it's all about which way you look x <a>lnk.example/PVcZ</a></div></div>
  <div style="position:absolute;left:9px;top:95px;width:152px;height:1px;background:var(--line)"></div>
  <div class="tweet" style="top:101px"><div class="avatar" role="img" aria-label="Profile photo"></div><div class="body"><b>Marla Penrick</b><br><span class="handle">@marlapenrickltd</span></div><div style="margin-top:4px">Going to miss waking up to this every day, but looking forward to getting back to London too.</div></div>
</aside>

<aside class="abs card partners">
  <h2 class="h" style="position:absolute;left:9px;top:9px;font-weight:400;font-size:11.5px">Partners</h2>
  <div style="position:absolute;left:9px;top:28px;width:156px;height:1px;background:var(--line)"></div>
  <div class="badge" style="left:12px;top:50px"></div><div class="badge" style="left:98px;top:50px"></div>
  <div class="badge" style="left:12px;top:92px"></div><div class="badge" style="left:98px;top:92px"></div>
  <div class="badge" style="left:12px;top:133px"></div><div class="badge" style="left:98px;top:133px"></div>
  <div class="badge" style="left:12px;top:174px"></div><div class="badge" style="left:98px;top:174px"></div>
  <div class="badge" style="left:12px;top:212px"></div><div class="badge" style="left:98px;top:212px"></div>
</aside>

<article class="abs card aud" style="left:54px">
  <div class="aud-photo" role="img" aria-label="Young woman in a checked shirt holding papers" style="background:linear-gradient(135deg,#e9e4dc,#b38e74 50%,#4d6a9c)"></div>
  <h3>Individual</h3>
  <p>You are a professional who is frustrated with your image.you want looking good to be easy,but don't know where to start.</p>
</article>
<article class="abs card aud" style="left:273px">
  <div class="aud-photo" role="img" aria-label="Smiling businesswoman in a white blouse" style="background:linear-gradient(135deg,#c9d6e0,#d6b09a 50%,#f2f2f2)"></div>
  <h3>Business</h3>
  <p>You are a medium to large sized business who wants your employees to project a more confident, professional image.</p>
</article>

<section class="abs card stories">
  <h2 class="h" style="position:absolute;left:13px;top:12px;font-weight:400">Success <em>Stories</em></h2>
  <div class="pol" style="left:14px;top:38px;transform:rotate(-3deg)"><div role="img" aria-label="Client portrait in a blue jacket" style="background:linear-gradient(#5a7a3a,#2a5fb8)"></div></div>
  <div class="quote" style="left:95px;top:40px">"I've never been a fashionista and my wardrobe was dominated by the colour black... my appearance in terms of make-up and clothing had become<i>Maria - HR Director</i><span>Read More</span></div>
  <div class="pol" style="left:222px;top:38px;transform:rotate(-2deg)"><div role="img" aria-label="Client portrait in a burgundy top" style="background:linear-gradient(#b7b0a4,#6e2a3a)"></div></div>
  <div class="quote" style="left:307px;top:40px">"I visited Marla for a 1 to 1 impact session. I've recently set up my own business and wanted to ensure that I was giving off the perfect image...<i>Maria - HR Director</i><span>Read More</span></div>
</section>

<aside class="abs card tips">
  <h2 class="h" style="position:absolute;left:9px;top:9px;font-weight:400;font-size:11.5px">Latest Tips <em>&amp; Videos</em></h2>
  <div style="position:absolute;left:9px;top:27px;width:156px;height:1px;background:var(--line)"></div>
  <div class="tip-img" style="top:38px;background:linear-gradient(135deg,#8a8a8a,#d9d9d9 50%,#b02030)" role="img" aria-label="Video thumbnail of the coach"></div>
  <div class="tip" style="top:40px">Networking made easy - top tips to network like a pro<span>Read More</span></div>
  <div class="tip-img" style="top:87px;background:linear-gradient(135deg,#2a2a2a,#8a6a4a 50%,#d0b080)" role="img" aria-label="Store interior thumbnail"></div>
  <div class="tip" style="top:89px">Stylemart Survival Guide - for Grown-Ups!<span>Read More</span></div>
</aside>

<section class="abs news">
  <h2>SUBSRIBE NEWSLETTER</h2>
  <p>Hey! Don't go without signing up because you'll miss out on exclusive offers, awesome tips, and weekly motivation in my fab newsletter*.</p>
</section>
<div class="abs field news-first">First Name</div>
<div class="abs field news-email">Email</div>
<div class="abs yes news-yes">YES<br>PLEASE</div>
<div class="abs news-sad">And tha'll make me a sad :-(</div>
<div class="abs news-social social"><i class="dot fb"></i><i class="dot tw"></i><i class="dot li"></i></div>

<footer class="abs footer">
  <span class="copy">Copyright © 2016 . Marla Penrick</span>
  <span class="links"><span>Privacy Policy</span><span>Terms Policy</span><span>Disclaimer</span></span>
</footer>
</body>
</html>
```